Graphic Design Vendora Book Description

There is a book on Vendora that is my competitor that has a large graphic design as part of the description for the book and I want a similar thing for my book to make it stand out more.

My competitors book is here: https://www.vendora-shop.example/Tidal-Lore-Starters-Grasping-Overview/dp/K31RTWP704/

My book is here: https://www.vendora-shop.example/Tidal-Lore-Groundwork-Workings-Interlacing/dp/K7Q2FXH58C/

You can see the kind of thing I am looking for on the book listing but I have attached an image below.

Thanks

Colin

```html
<!DOCTYPE html>
<html lang="en">
<head>
<meta charset="utf-8">
<title>Quantum Physics – Book Description Graphic</title>
<link rel="stylesheet" href="https://fonts.googleapis.com/css2?family=Bebas+Neue&family=Oswald:wght@300;400;700&family=Montserrat:wght@400;800;900&family=Poppins:wght@400;500;700&display=swap">
<style>
:root{
  --space-deep:#0d1330;
  --space-mid:#26306a;
  --earth-dark:#1a1410;
  --yellow:#f0e62e;
  --yellow-soft:#f5ec4c;
  --navy:#0b1a4a;
  --cyan:#3fd8ff;
  --red:#d80f0f;
  --white:#ffffff;
  --ink:#1d1d1d;
  --pill-line:#c9c9c9;
}
*{box-sizing:border-box;margin:0;padding:0}
html,body{width:723px;height:1200px;overflow:hidden;background:#fff}
.canvas{position:relative;width:723px;height:1200px;overflow:hidden;background:var(--white);font-family:"Poppins",sans-serif}

.hero{position:absolute;left:0;top:0;width:723px;height:907px;
  background:
   radial-gradient(ellipse 70% 30% at 40% 40%, rgba(216,130,60,.55), transparent 70%),
   radial-gradient(ellipse 90% 40% at 50% 75%, rgba(60,40,30,.9), transparent 75%),
   linear-gradient(180deg,var(--space-deep) 0%,var(--space-mid) 30%,#4a3a4a 45%,#2a2030 60%,var(--earth-dark) 80%,#17131a 100%);}

.headline{position:absolute;left:366px;top:44px;width:350px;line-height:1}
.headline .lead{font-family:"Bebas Neue",sans-serif;font-size:56px;color:var(--white);letter-spacing:.5px;display:block;height:52px;text-shadow:0 0 6px rgba(120,200,255,.6)}
.headline .accent{font-family:"Montserrat",sans-serif;font-weight:900;font-size:27px;color:var(--yellow);display:block;line-height:26px;margin-top:2px}
.headline .into{font-family:"Montserrat",sans-serif;font-weight:800;font-size:24.5px;color:var(--white);display:block;margin-top:2px;letter-spacing:-.3px}
.headline .topic{font-family:"Montserrat",sans-serif;font-weight:900;font-size:50px;color:var(--navy);display:block;line-height:50px;letter-spacing:-.5px;
  text-shadow:0 0 2px var(--cyan),0 0 8px var(--cyan),0 0 14px rgba(63,216,255,.7)}

.mockup{position:absolute}
.mockup.stack{left:80px;top:88px;width:270px;height:280px;background:linear-gradient(135deg,var(--yellow-soft),#d8cc1a);transform:skewY(3deg)}
.mockup.open-book{left:175px;top:365px;width:325px;height:195px;background:linear-gradient(90deg,#e8e8ec,#ffffff 48%,#d9d9de 50%,#f6f6f8);transform:rotate(-3deg)}
.mockup.back-cover{left:525px;top:378px;width:142px;height:185px;background:linear-gradient(160deg,var(--yellow-soft),#d6ca18)}

.badge{position:absolute;border-radius:50%;background:radial-gradient(circle at 40% 35%,#f02a1e,var(--red) 60%,#a00808);color:var(--white);text-align:center;display:flex;flex-direction:column;justify-content:center;align-items:center}
.badge.ideal{left:52px;top:358px;width:164px;height:160px;box-shadow:0 0 0 6px var(--red)}
.badge.ideal .small{font-family:"Poppins",sans-serif;font-size:11.5px;letter-spacing:2px}
.badge.ideal .big{font-family:"Montserrat",sans-serif;font-weight:900;font-size:11.5px;line-height:13px}
.badge.ideal .big .hl{color:var(--yellow)}
.badge.gift{left:596px;top:278px;width:94px;height:92px;transform:rotate(18deg)}
.badge.gift .small{font-family:"Montserrat",sans-serif;font-weight:800;font-size:7px;line-height:8px}
.badge.gift .big{font-family:"Bebas Neue",sans-serif;font-size:18px;line-height:15px;color:var(--yellow)}

.features{position:absolute;left:59px;top:585px;display:flex;gap:13px}
.feature{width:142px;height:246px;border:1px solid var(--yellow);border-radius:10px;overflow:hidden;background:linear-gradient(180deg,rgba(20,18,30,.75),rgba(28,20,14,.9))}
.feature.alt{border-color:var(--white)}
.feature-title{height:107px;background:var(--yellow);display:flex;flex-direction:column;justify-content:center;align-items:center;text-align:center;font-family:"Oswald",sans-serif;color:var(--ink);line-height:.95}
.feature.alt .feature-title{background:var(--white)}
.feature-title .thin{font-weight:300;font-size:21px}
.feature-title .bold{font-weight:700;font-size:21px;letter-spacing:-.3px}
.feature p{color:var(--white);font-size:12.5px;line-height:15.6px;text-align:center;padding:10px 8px 0}

.contents-band{position:absolute;left:233px;top:885px;width:449px;height:41px;background:var(--yellow);border-radius:0 6px 6px 0;
  font-family:"Montserrat",sans-serif;font-size:22px;color:var(--ink);display:flex;align-items:center;padding-left:53px;letter-spacing:1px;font-weight:400;white-space:nowrap}
.contents-band b{font-weight:900;margin-left:7px}
.mockup.front{left:43px;top:882px;width:224px;height:290px;background:linear-gradient(160deg,var(--yellow-soft),#d2c414);clip-path:polygon(0 3%,84% 0,100% 84%,17% 100%)}

.chapters{position:absolute;left:286px;top:943px;list-style:none}
.chapters li{height:18px;margin-bottom:9.8px;border:1px solid var(--pill-line);border-radius:9px;font-family:"Poppins",sans-serif;font-weight:500;font-size:12.5px;color:var(--ink);padding-left:13px;line-height:16px;white-space:nowrap}
</style>
</head>
<body>
<div class="canvas">
  <section class="hero" role="img" aria-label="Space background with a glowing planet Earth, stars and atom orbits"></section>

  <div class="mockup stack" role="img" aria-label="Two stacked yellow paperback copies of the Quantum Physics book"></div>
  <div class="mockup open-book" role="img" aria-label="Open book showing the introduction and first chapter pages"></div>
  <div class="mockup back-cover" role="img" aria-label="Back cover of the book with its description"></div>

  <h1 class="headline">
    <span class="lead">EMBARK ON A</span>
    <span class="accent">MIND-BENDING<br>JOURNEY</span>
    <span class="into">INTO THE REALM OF</span>
    <span class="topic">QUANTUM<br>PHYSICS</span>
  </h1>

  <div class="badge ideal">
    <span class="small">IDEAL FOR</span>
    <span class="big"><span class="hl">SCIENCE STUDENTS,</span><br>QUANTUM<br>COMPUTING<br>ENTHUSIASTS</span>
  </div>
  <div class="badge gift">
    <span class="small">PERFECT<br>GIFT FOR THE</span>
    <span class="big">SCIENCE<br>LOVER</span>
  </div>

  <div class="features">
    <article class="feature">
      <h2 class="feature-title"><span class="thin">HISTORY</span><span class="bold">OF QUANTUM<br>MECHANICS</span></h2>
      <p>Explore the fascinating history of quantum mechanics and the brilliant minds behind its development</p>
    </article>
    <article class="feature alt">
      <h2 class="feature-title"><span class="thin">FUNDAMENTAL</span><span class="bold">PRINCIPLES OF<br>WAVE-PARTICLE</span></h2>
      <p>Grasp the fundamental principles of wave-particle duality, quantum states, and the uncertainty principle</p>
    </article>
    <article class="feature">
      <h2 class="feature-title"><span class="thin">QUANTUM</span><span class="bold">ENTANGLEMENT</span></h2>
      <p>Dive into the strange and counterintuitive world of quantum entanglement and its implications for reality itself</p>
    </article>
    <article class="feature alt">
      <h2 class="feature-title"><span class="thin">QUANTUM</span><span class="bold">COMPUTING TO<br>CRYPTOGRAPHY</span></h2>
      <p>Learn about the cutting-edge applications of quantum mechanics, from quantum computing to cryptography</p>
    </article>
  </div>

  <div class="contents-band">IN THIS BOOK <b>YOU WILL FIND</b></div>
  <div class="mockup front" role="img" aria-label="Front cover of the yellow Quantum Physics paperback"></div>

  <ul class="chapters">
    <li style="width:226px">The Quantum World Unveiled</li>
    <li style="width:384px">The Mathematical Symphony of Quantum Mechanics</li>
    <li style="width:226px">Beyond Classical Boundaries</li>
    <li style="width:226px">Quantum Mechanics at Work</li>
    <li style="width:325px">Bridging Quantum Mechanics and Relativity</li>
    <li style="width:343px">Quantum Paradoxes and Thought Experiments</li>
    <li style="width:307px">Quantum Mechanics for the Curious Mind</li>
    <li style="width:374px">Quantum Mechanics Demystified - A Practical Guide</li>
  </ul>
</div>
</body>
</html>
```